Harbor Crest Vitality.com Landing Page

Create a well designed home/landing page using that communicates the feeling of Harbor Crest Vitality with this sections that scroll from top to bottom -
Top section - Displays "Harbor Crest Vitality" with space for embedded YouTube video.

The following sections follow the top section -
Assess your current Harbor Crest Vitality. Complete our free life balance assessment to identify key areas where you you will most benefit.
"Learn more" call to action button

Create a Harbor Crest Vitality Learning Portal account. Get a 14 day free trial to a wealth of learning activities, motivational videos and professional presentations on our learning portal designed specifically to address the eight essential areas of Harbor Crest Vitality.
"Register now" call to action button

Get weekly reports on your progress and goal achievement. Celebrate your success each week as you review your progress on each life balance area.

Appropriate royalty free photos and graphics that fit the chosen theme you recommend.

I'm reviewing the designs. I realize that I need to clarify that Harbor Crest Vitality focuses on eight areas, not just physical fitness and meditation. Spirituality and Sense of Purpose; Fitness and Health; Relationships; Personal Finance; Recreation and Fun; Physical Environment; Personal Development and Learning; Work and Career

1 page

33a6d7
00a990
9bcb3c
2f73b3

```html
<!DOCTYPE html>
<html lang="en">
<head>
<meta charset="utf-8">
<title>Harbor Crest Vitality</title>
<link rel="stylesheet" href="https://fonts.googleapis.com/css2?family=Raleway:wght@400;500;600;700;800&display=swap">
<style>
  :root {
    --green: #9bcb3c;
    --white: #ffffff;
    --ink: #333333;
    --line: #c9c9c9;
    --hero-dark: #1c1a18;
  }
  * { box-sizing: border-box; margin: 0; padding: 0; }
  html, body { width: 872px; height: 1200px; overflow: hidden; background: var(--white); }
  body { font-family: "Raleway", sans-serif; color: var(--ink); position: relative; }

  .hero {
    position: absolute; left: 0; top: 0; width: 872px; height: 348px;
    background:
      linear-gradient(90deg, rgba(40,28,18,.2), rgba(20,20,22,.35)),
      linear-gradient(135deg, #5a3e22 0%, #2e2a27 35%, #3a3632 60%, #2a2624 100%);
    overflow: hidden;
  }
  .hero-collage { position: absolute; inset: 0; }
  .hero-title {
    position: absolute; left: 109px; top: 96px; width: 320px;
    font-weight: 800; font-size: 31px; line-height: 37px; letter-spacing: 1.2px;
    color: var(--white);
  }
  .hero-button {
    position: absolute; left: 109px; top: 187px; width: 85px; height: 27px;
    background: var(--green); color: var(--white); border-radius: 2px;
    font-size: 9.5px; font-weight: 500; display: flex; align-items: center; justify-content: center;
  }
  .hero-video {
    position: absolute; left: 440px; top: 84px; width: 323px; height: 192px;
    border: 3px solid var(--white);
    background: linear-gradient(180deg, #6f8b86 0%, #b9a76f 45%, #e29a3c 62%, #2b1d12 78%, #1b140f 100%);
  }
  .hero-video svg { position: absolute; left: 50%; top: 44%; transform: translate(-50%, -50%); }

  .feature {
    position: absolute; left: 109px; width: 654px; height: 179px;
    border: 1px solid var(--line); border-radius: 2px; background: var(--white);
    display: flex;
  }
  .feature-photo { width: 246px; height: 100%; flex: none; }
  .feature-body { flex: 1; padding: 0 29px; }
  .feature-title { font-size: 13px; font-weight: 600; line-height: 13.5px; margin-bottom: 12px; }
  .feature-text { font-size: 9.5px; line-height: 13px; font-weight: 500; margin-bottom: 10px; }
  .pill-button {
    display: inline-flex; align-items: center; justify-content: center;
    height: 23px; padding: 0 9px; border-radius: 12px;
    background: var(--green); color: var(--white);
    font-size: 8.5px; font-weight: 700; letter-spacing: .4px;
  }

  .feature-assess { top: 421px; }
  .feature-assess .feature-body { padding-top: 30px; }
  .photo-meditation { background: linear-gradient(160deg, #b98a72 0%, #8a4b34 45%, #3a2218 80%, #1e120c 100%); }

  .feature-portal { top: 639px; }
  .feature-portal .feature-body { padding-top: 30px; }
  .photo-sunset { background: radial-gradient(circle at 60% 55%, #fff4b0 0%, #f7c544 25%, #e98a2a 55%, #c4566a 85%), #222; }

  .feature-reports { top: 856px; }
  .feature-reports .feature-body { padding-top: 31px; }
  .photo-summit { background: linear-gradient(180deg, #5d6f86 0%, #9aa7b6 35%, #d79a96 48%, #4c5f78 65%, #6f5a45 85%, #3e3226 100%); }

  .footer {
    position: absolute; left: 0; top: 1112px; width: 872px; height: 88px;
    background: var(--green); color: var(--white);
  }
  .footer-heading { position: absolute; left: 0; right: 0; top: 10px; text-align: center; font-size: 9.5px; font-weight: 600; }
  .footer-social { position: absolute; left: 0; right: 0; top: 31px; display: flex; justify-content: center; gap: 9.5px; }
  .social-dot { width: 18px; height: 18px; border-radius: 50%; background: var(--white); }
  .footer-copy { position: absolute; left: 108px; top: 62px; font-size: 7.5px; font-weight: 500; }
  .footer-links { position: absolute; right: 110px; top: 62px; font-size: 7.5px; font-weight: 500; }
</style>
</head>
<body>
  <header class="hero">
    <div class="hero-collage" role="img" aria-label="Collage of photos showing people working, exercising, relaxing and spending time with family and friends"></div>
    <h1 class="hero-title">Harbor Crest Vitality</h1>
    <div class="hero-button">GET STARTED</div>
    <div class="hero-video" role="img" aria-label="Video: group of friends jumping in silhouette at sunset on a beach">
      <svg width="34" height="34" viewBox="0 0 34 34" aria-hidden="true">
        <circle cx="17" cy="17" r="15" fill="none" stroke="#ffffff" stroke-width="2"/>
        <path d="M13 10 L25 17 L13 24 Z" fill="#ffffff"/>
      </svg>
    </div>
  </header>

  <section class="feature feature-assess">
    <div class="feature-photo photo-meditation" role="img" aria-label="Woman meditating in lotus pose facing a sunlit forest"></div>
    <div class="feature-body">
      <h2 class="feature-title">Assess your current Harbor Crest Vitality.</h2>
      <p class="feature-text">Complete our free life balance assessment to identify key areas<br>where you you will most benefit.</p>
      <span class="pill-button">Learn More</span>
    </div>
  </section>

  <section class="feature feature-portal">
    <div class="feature-body">
      <h2 class="feature-title">Create a Harbor Crest Vitality Learning Portal<br>account.</h2>
      <p class="feature-text">Get a 14 day free trial to a wealth of learning activities, motivational videos and professional presentations on our learning portal designed specifically to address the eight essential areas of Harbor Crest Vitality.</p>
      <span class="pill-button" style="padding:0 12px">Register Now</span>
    </div>
    <div class="feature-photo photo-sunset" role="img" aria-label="Silhouette of a woman stretching her arms on a beach at sunset"></div>
  </section>

  <section class="feature feature-reports">
    <div class="feature-photo photo-summit" role="img" aria-label="Man with outstretched arms standing on a rocky summit under a cloudy sky"></div>
    <div class="feature-body">
      <h2 class="feature-title">Get weekly reports on your progress and goal<br>achievement.</h2>
      <p class="feature-text">Celebrate your success each week as you review your progress on<br>each life balance area.</p>
      <span class="pill-button">Learn More</span>
    </div>
  </section>

  <footer class="footer">
    <div class="footer-heading">FOLLOW US</div>
    <div class="footer-social">
      <span class="social-dot" aria-label="Social link 1"></span>
      <span class="social-dot" aria-label="Social link 2"></span>
      <span class="social-dot" aria-label="Social link 3"></span>
      <span class="social-dot" aria-label="Social link 4"></span>
      <span class="social-dot" aria-label="Social link 5"></span>
    </div>
    <div class="footer-copy">Harborcrestvitality.com © 2020. All Rights Reserved.</div>
    <div class="footer-links">Terms and Conditions | Privacy Policy</div>
  </footer>
</body>
</html>
```